Vulmaro.com needs a Mobile FIRST Site

Vulmaro.com is an insurance broker based in Panama City, Panama that plans to sell car and motorcycle insurance online.

We need to design a total of 5 pages (two of those are A/B test pages). The site will be responsive and will be programmed in React. We will be using Ant Design´s library to code Vulmaro.com. Keep in mind that we are using Ant Design to program the site´s functions, not to create the "look and feel" of the site, that is obviously your job. You can learn more about Ant Design here... https://plinketo.design/

We have created wireframes for the app. Please follow and keep in mind the instructions in the wireframes. You can change things here and there as long as the core functions and goals stay intact. We have uploaded the wireframes along with the company logo and color.

We are planning to A/B test the site´s home page so we need to design two homepages. You can find homepage A and B in the wireframes provided.

We speak Spanish in Panama but you can design the site in English. We can change the text once we receive the designs.

Target Market(s)

25-45 year olds who own a car or motorcylcle and own a credit card.

Industry/Entity Type

Insurance

Font styles to use
Sans Serif

Requirements
Must have
• Follow the wireframes provided and the logo colors.
Nice to have
• Please look at the Image I´ve uploaded from DeskHarbor, use it as reference to create HomePage A.

```html
<!DOCTYPE html>
<html lang="es">
<head>
<meta charset="utf-8">
<title>Vulmaro.com – Mobile screens</title>
<link href="https://fonts.googleapis.com/css2?family=Roboto:wght@300;400;500&display=swap" rel="stylesheet">
<style>
  :root{
    --purple:#5b2a86;
    --purple-deep:#4a1f73;
    --blue:#4f63c4;
    --ink:#3a2a55;
    --muted:#8a84a0;
    --line:#c9b8dc;
    --bg:#ffffff;
    --screen:#ffffff;
    --grad:linear-gradient(90deg,var(--blue),var(--purple));
  }
  *{box-sizing:border-box;margin:0;padding:0}
  html,body{width:1200px;height:805px;overflow:hidden;background:var(--bg);font-family:"Roboto",Arial,sans-serif;color:var(--ink)}
  .canvas{position:relative;width:1200px;height:805px}
  .screen{position:absolute;width:200px;height:340px;top:232px;background:var(--screen);border:1px solid #e3dfea;box-shadow:0 6px 18px rgba(40,20,70,.12);overflow:hidden;display:flex;flex-direction:column}
  .screen--login{width:260px;height:420px;top:192px;left:470px;align-items:center}
  .s1{left:20px}.s2{left:245px}.s4{left:755px}.s5{left:980px}

  .steps{height:46px;background:var(--grad);display:flex;justify-content:space-between;align-items:flex-end;padding:0 14px;flex-shrink:0}
  .steps span{color:#fff;font-size:10.5px;padding-bottom:5px;border-bottom:2px solid transparent}
  .steps .is-active{border-bottom-color:#fff}

  .vehicle-switch{display:flex;margin:7px auto 0;border:1px solid var(--purple);border-radius:3px;width:158px;height:17px;overflow:hidden;flex-shrink:0}
  .vehicle-switch span{flex:1;display:flex;align-items:center;justify-content:center;gap:4px;font-size:9.5px;color:var(--purple)}
  .vehicle-switch .is-active{background:var(--purple);color:#fff}
  .vehicle-switch i{display:inline-block;width:16px;height:6px;border-radius:3px 5px 2px 2px;background:currentColor}

  /* form */
  .driver-card{margin:30px 16px 0;border:1px solid var(--line);border-bottom:none;flex:1;display:flex;flex-direction:column}
  .driver-card__head{height:25px;background:var(--purple);color:#fff;display:flex;align-items:center;padding:0 8px;gap:14px;font-size:7px}
  .driver-card__head .plan{margin-left:auto;line-height:1.05}
  .driver-card__head svg{flex-shrink:0}
  .form{padding:7px 5px;font-size:6px;color:var(--muted)}
  .form h3{font-size:9.5px;font-weight:400;color:var(--purple)}
  .field{margin-top:9px}
  .field b{display:block;font-weight:500;font-size:7px;color:var(--ink);border-bottom:1px solid var(--line);padding:4px 0 2px;width:116px}
  .radios{display:flex;gap:28px;margin-top:14px;font-size:6px;color:var(--ink)}
  .radios span::before{content:"";display:inline-block;width:7px;height:7px;border-radius:50%;background:var(--purple-deep);margin-right:8px;vertical-align:middle}
  .id-row{display:flex;gap:8px;margin-top:16px}
  .box{border:1px solid var(--purple);height:11px;font-size:6.5px;color:var(--ink);display:flex;align-items:center;padding:0 3px}
  .dates{display:flex;align-items:center;gap:4px;margin-top:4px}

  /* plans */
  .plans{display:flex;gap:4px;margin:17px 12px 0 12px;flex:1}
  .plan-card{flex:1;border:1px solid var(--line);border-bottom:none;padding:3px 3px 0;display:flex;flex-direction:column}
  .plan-card__img{height:46px;border-radius:2px;flex-shrink:0}
  .img-car-red{background:linear-gradient(135deg,#e04a4a,#b31c25)}
  .img-car-orange{background:linear-gradient(135deg,#f1a24a,#d4702a)}
  .img-moto-dark{background:linear-gradient(135deg,#5b5b60,#1e1e22)}
  .img-moto-yellow{background:linear-gradient(135deg,#f0d23a,#2a2a2a)}
  .price{font-size:9px;color:var(--purple);margin:6px 0 0 2px;padding-bottom:6px;border-bottom:1px solid var(--line)}
  .metric{font-size:7px;color:var(--purple);margin-top:8px}
  .bar{height:8px;border:1px solid var(--purple);margin-top:1px;background:#fff}
  .bar i{display:block;height:100%;width:72%;background:var(--grad)}
  .benefits{font-size:9px;color:var(--purple);margin-top:14px;border-top:1px solid var(--line);padding-top:5px}
  .benefits-text{font-size:4px;line-height:1.25;color:var(--muted);margin-top:3px}
  .buy{margin:auto auto 6px;background:var(--purple);color:#fff;font-size:7.5px;font-weight:500;border-radius:3px;padding:1px 5px}
  .pager{position:absolute;right:4px;top:198px;width:4px;height:4px;border:1px solid var(--blue);border-radius:50%}

  /* login */
  .brand{margin-top:108px;display:flex;align-items:center;gap:8px;color:var(--purple);font-size:36px;font-weight:500;letter-spacing:-.5px}
  .brand i{width:14px;height:14px;background:var(--purple)}
  .btn{width:182px;height:42px;border-radius:21px;font-size:18px;display:flex;align-items:center;justify-content:center}
  .btn--login{margin-top:138px;background:var(--grad);color:#fff}
  .hint{font-size:9px;color:var(--muted);margin:15px 0 6px}
  .btn--register{border:2px solid var(--purple);color:var(--purple)}

  /* pay */
  .claim{text-align:center;font-size:12px;font-weight:400;color:var(--purple);margin-top:20px}
  .claim-text{font-size:11.5px;color:var(--purple);margin:10px 16px 0;line-height:1.3;font-weight:400}
  .policy{margin:12px 16px 20px;border:1px solid var(--line);flex:1;display:flex;flex-direction:column}
  .policy__bar{height:17px;background:var(--grad)}
  .policy h4{font-size:9px;font-weight:400;color:var(--purple);text-align:center;margin-top:8px}
  .policy__doc{width:38px;height:38px;margin:8px auto 14px;border-radius:3px;background:linear-gradient(160deg,#7ea8e8,#3c6cc4)}
  .actions{list-style:none;padding-left:36px}
  .actions li{display:flex;align-items:center;gap:6px;font-size:9.5px;color:var(--purple);margin-bottom:9px}
</style>
</head>
<body>
<main class="canvas">

  <!-- Datos: formulario del conductor -->
  <section class="screen s1">
    <nav class="steps"><span>Elige</span><span class="is-active">Datos</span><span>Paga</span></nav>
    <div class="vehicle-switch"><span class="is-active"><i></i>Carros</span><span><i></i>Motos</span></div>
    <div class="driver-card">
      <div class="driver-card__head">
        <svg width="10" height="8" viewBox="0 0 10 8"><path d="M9 4H1M4 1 1 4l3 3" stroke="#fff" fill="none" stroke-width="1.2"/></svg>
        <svg width="22" height="8" viewBox="0 0 22 8"><path d="M1 6h20V4l-5-1-3-2H7L4 3 1 4z" fill="#fff"/></svg>
        <span class="plan">Tarvina Plan B<br>$150</span>
      </div>
      <div class="form">
        <h3>Datos del conductor</h3>
        <div>Nombre Completo</div>
        <div class="field"><b>Marcelo Ruiz</b></div>
        <div class="field">E- mail<b>marceloruiz@correo.test</b></div>
        <div class="field">No, de Identificación</div>
        <div class="radios"><span>Cedula</span><span>Pasaporte</span></div>
        <div class="id-row">
          <div class="box" style="width:36px">00&nbsp;<svg width="10" height="9" viewBox="0 0 10 9" style="margin-left:auto"><path d="M0 0h10" stroke="#5b2a86"/><path d="M2 3h6L5 8z" fill="#5b2a86"/></svg></div>
          <div class="box" style="width:36px;margin-left:12px"></div>
          <div class="box" style="width:36px;margin-left:12px"></div>
        </div>
        <div class="field">Fecha de Nacimiento</div>
        <div class="dates"><div class="box">DD</div>/<div class="box">MM</div>/<div class="box">AA</div></div>
      </div>
    </div>
  </section>

  <!-- Elige: carros -->
  <section class="screen s2">
    <nav class="steps"><span>Elige</span><span class="is-active">Datos</span><span>Paga</span></nav>
    <div class="vehicle-switch"><span class="is-active"><i></i>Carros</span><span><i></i>Motos</span></div>
    <div class="plans">
      <article class="plan-card">
        <div class="plan-card__img img-car-red" role="img" aria-label="Foto de un carro rojo"></div>
        <div class="price">$150.00</div>
        <div class="metric">xxx</div><div class="bar"><i></i></div>
        <div class="metric">xxx</div><div class="bar"><i></i></div>
        <div class="metric">xxx</div><div class="bar"><i></i></div>
        <div class="benefits">Beneficios</div>
        <p class="benefits-text">Lorem ipsum dolor sit amet, consectetuer adipiscing elit, sed diam nonummy nibh euismod tincidunt ut laoreet dolore magna aliquam erat.</p>
        <span class="buy">COMPRAR</span>
      </article>
      <article class="plan-card">
        <div class="plan-card__img img-car-orange" role="img" aria-label="Foto de un carro naranja"></div>
        <div class="price">$170.00</div>
        <div class="metric">xxx</div><div class="bar"><i></i></div>
        <div class="metric">xxx</div><div class="bar"><i></i></div>
        <div class="metric">xxx</div><div class="bar"><i></i></div>
        <div class="benefits">Beneficios</div>
        <p class="benefits-text">Lorem ipsum dolor sit amet, consectetuer adipiscing elit, sed diam nonummy nibh euismod tincidunt ut laoreet dolore magna aliquam erat.</p>
        <span class="buy">COMPRAR</span>
      </article>
    </div>
    <span class="pager"></span>
  </section>

  <!-- Inicio de sesión -->
  <section class="screen screen--login">
    <div class="brand"><i></i>Vulmaro.com</div>
    <a class="btn btn--login">LOGIN</a>
    <p class="hint">Don't have an account?</p>
    <a class="btn btn--register">REGISTER</a>
  </section>

  <!-- Elige: motos -->
  <section class="screen s4">
    <nav class="steps"><span>Elige</span><span>Datos</span><span class="is-active">Paga</span></nav>
    <div class="vehicle-switch"><span><i></i>Carros</span><span class="is-active"><i></i>Motos</span></div>
    <div class="plans">
      <article class="plan-card">
        <div class="plan-card__img img-moto-dark" role="img" aria-label="Foto de una motocicleta negra"></div>
        <div class="price">$150.00</div>
        <div class="metric">xxx</div><div class="bar"><i></i></div>
        <div class="metric">xxx</div><div class="bar"><i></i></div>
        <div class="metric">xxx</div><div class="bar"><i></i></div>
        <div class="benefits">Beneficios</div>
        <p class="benefits-text">Lorem ipsum dolor sit amet, consectetuer adipiscing elit, sed diam nonummy nibh euismod tincidunt ut laoreet dolore magna aliquam erat.</p>
        <span class="buy">COMPRAR</span>
      </article>
      <article class="plan-card">
        <div class="plan-card__img img-moto-yellow" role="img" aria-label="Foto de una motocicleta deportiva amarilla"></div>
        <div class="price">$150.00</div>
        <div class="metric">xxx</div><div class="bar"><i></i></div>
        <div class="metric">xxx</div><div class="bar"><i></i></div>
        <div class="metric">xxx</div><div class="bar"><i></i></div>
        <div class="benefits">Beneficios</div>
        <p class="benefits-text">Lorem ipsum dolor sit amet, consectetuer adipiscing elit, sed diam nonummy nibh euismod tincidunt ut laoreet dolore magna aliquam erat.</p>
        <span class="buy">COMPRAR</span>
      </article>
    </div>
    <span class="pager"></span>
  </section>

  <!-- Paga -->
  <section class="screen s5">
    <nav class="steps"><span>Elige</span><span>Datos</span><span class="is-active">Paga</span></nav>
    <h2 class="claim">CLAIM AQUI</h2>
    <p class="claim-text">Lorem ipsum dolor sit amet, consectetuer adipiscing elit,</p>
    <div class="policy">
      <div class="policy__bar"></div>
      <h4>Tu polza de seguro..</h4>
      <div class="policy__doc" role="img" aria-label="Ilustración de documento de póliza"></div>
      <ul class="actions">
        <li><svg width="18" height="16" viewBox="0 0 18 16"><rect x="1" y="3" width="11" height="12" fill="none" stroke="#5b2a86"/><path d="M7 10 15 2l2 2-8 8-3 1z" fill="none" stroke="#5b2a86"/></svg>Cambiar datos</li>
        <li><svg width="18" height="14" viewBox="0 0 18 14"><rect x="1" y="1" width="16" height="12" fill="none" stroke="#5b2a86"/><path d="m1 1 8 7 8-7" fill="none" stroke="#5b2a86"/></svg>Enviar a otro e-mail</li>
        <li><svg width="18" height="16" viewBox="0 0 18 16"><path d="M9 1v9M5 6l4 4 4-4" fill="none" stroke="#5b2a86" stroke-width="2"/><path d="M1 11v4h16v-4" fill="none" stroke="#5b2a86" stroke-width="2"/></svg>Descargar</li>
      </ul>
    </div>
  </section>

</main>
</body>
</html>
```